Consumer Product Goods (Food) website

We need a simple, but clean and modern website for our new food branded company called Brightfern Foods.

Need a website that company can easily update. I added company logo and some images of our products. I added 1 package design of our products that's available now in the retail stores.

Company currently has 1 item but will be adding up to 5 items witin a few months. So need a website we can easily add new products.
Updates

Project Deadline Extended
Reason: We're guaranteeing payment and wanted to give more time for others to submit.

Target Market(s)

Customers that are seeking new adventurous novelty Asian foods.

Industry/Entity Type

Retail

Coding

Coded - Design and coding required

Number of Pages Required

3 page

Requirements
Must have
• I would like to have 3 pages: Homepage, Products Page, and Contact Us.
Nice to have
• I would like a nice visually clean and modern looking homepage. As you can see from the package design, it has a dark tone, so if we can try to make the website a dark blackgroup. I uploaded the dark background we used in our package. Maybe have the 3 different dumplings rotating images on the homepage.
• Products Page should have just 1 product right now; Kimchi & Pork dumplings. Maybe have like pic of the package design and have space for a briefly summary of product, ingredient list and nutrition fact. Should be a page where i can add more products to this page.
• Contact Us page can simply have map, email addres, and phone #.
• would be nice to have where the website is responsive to PC, tablet, and mobile phones

```html
<!DOCTYPE html>
<html lang="en">
<head>
<meta charset="utf-8">
<title>Brightfern Foods</title>
<link rel="stylesheet" href="https://fonts.googleapis.com/css2?family=Montserrat:wght@400;500;600;700&family=Open+Sans:ital,wght@0,400;0,600;0,700;1,400&display=swap">
<style>
:root{
  --green:#7dc21e;
  --green-dark:#69a817;
  --ink:#2a2624;
  --paper:#eeebe2;
  --paper-line:#d4d0c6;
  --wood-1:#3a332d;
  --wood-2:#1f1b18;
  --footer:#272324;
  --footer-line:#3a3536;
  --bottom:#1d1a1a;
  --muted:#b9b4ad;
  --white:#ffffff;
}
*{box-sizing:border-box;margin:0;padding:0}
html,body{width:1200px;height:2264px;overflow:hidden}
body{position:relative;background:var(--paper);font-family:"Open Sans",Arial,sans-serif;color:var(--ink)}
.abs{position:absolute}

/* hero */
.hero{left:0;top:0;width:1200px;height:630px;overflow:hidden}
.hero-photo{position:absolute;inset:0;background:radial-gradient(ellipse 420px 330px at 600px 300px,#e9e3d0 0%,#b9b1a0 35%,#2c2825 62%),linear-gradient(90deg,#3b302a,#5a4a3e 50%,#3b302a)}
.topbar{position:absolute;left:0;top:0;width:1200px;height:115px;background:rgba(30,27,25,.78)}
.logo-tab{position:absolute;left:100px;top:0;width:190px;height:187px;background:var(--white);border-bottom:7px solid var(--green);clip-path:polygon(0 0,100% 0,100% 88%,50% 100%,0 88%);display:flex;flex-direction:column;align-items:center;padding-top:26px;gap:14px}
.logo-dot{width:64px;height:64px;border-radius:50%;background:var(--green)}
.logo-name{font-family:"Montserrat",sans-serif;font-weight:700;font-size:18px;line-height:1.15;color:var(--ink);text-align:center;text-transform:uppercase}
.nav{position:absolute;top:41px;left:428px;display:flex;font-family:"Montserrat",sans-serif;font-weight:700;font-size:14px;color:var(--white)}
.nav a{color:var(--white);text-decoration:none;height:33px;line-height:33px;padding:0 21px;border-radius:17px;text-transform:uppercase}
.nav a.active{background:var(--green)}
.call{position:absolute;left:923px;top:32px;display:flex;gap:14px;color:var(--white)}
.call-icon{width:52px;height:51px;border-radius:8px;background:rgba(255,255,255,.16);display:flex;align-items:center;justify-content:center}
.call-text{font-size:14px;line-height:20px;padding-top:2px}
.call-text b{font-weight:700;font-size:15px}
.caption{position:absolute;left:0;top:330px;width:500px;height:87px;background:rgba(25,22,20,.7)}
.caption h1{position:absolute;left:100px;top:22px;font-weight:700;font-size:33px;color:var(--white);letter-spacing:-.3px;white-space:nowrap}
.caption-slash{position:absolute;left:478px;top:328px}

/* notches */
.notch{position:absolute;left:0;width:1200px;display:block}

/* section heads */
.sec-title{position:absolute;left:0;width:1200px;text-align:center;font-family:"Montserrat",sans-serif;font-weight:600;font-size:30px}
.sec-title em{font-style:normal;color:var(--green)}
.mark{position:absolute;width:22px;height:22px;border-radius:50%;background:#9c978f;left:589px}

/* about */
.about-text{left:180px;top:748px;width:840px;text-align:center;font-size:12px;line-height:23px;color:#4a4643}
.btn-more{left:536px;top:873px;width:128px;height:30px;border:1.5px solid var(--ink);border-radius:15px;display:flex;overflow:hidden;font-size:13px;font-weight:700}
.btn-more span{flex:1;line-height:27px;text-align:center}
.btn-more i{width:30px;background:var(--ink);display:flex;align-items:center;justify-content:center}

/* products */
.products{left:0;top:954px;width:1200px;height:584px;background:linear-gradient(100deg,var(--wood-1),var(--wood-2) 45%,#332c27 75%,var(--wood-2))}
.products .sec-title{color:var(--white);top:58px}
.prod-rule{left:385px;top:113px;width:430px;height:1px;background:rgba(255,255,255,.35)}
.product{position:absolute;width:340px;text-align:center;top:160px}
.product-photo{width:220px;height:220px;margin:0 auto;border-radius:50%;border:6px solid var(--green);background:radial-gradient(circle at 50% 55%,#e7e1cd 0,#b8ae98 28%,#2b2623 52%,#3b332d 100%)}
.product h3{margin-top:24px;font-family:"Montserrat",sans-serif;font-weight:500;font-size:26px;line-height:36px;color:var(--white);height:72px}
.plus{width:36px;height:36px;margin:14px auto 0;background:var(--green);border-radius:3px;display:flex;align-items:center;justify-content:center}
.slide-arrow{position:absolute;top:309px;width:42px;height:42px;border-radius:8px;background:rgba(255,255,255,.2);display:flex;align-items:center;justify-content:center}

/* testimonials */
.avatar{left:559px;top:1678px;width:90px;height:90px;border-radius:50%;border:4px solid #dcd8cf;background:linear-gradient(160deg,#d8dde2,#9aa4ad)}
.client-name{left:0;top:1792px;width:1200px;text-align:center;font-weight:700;font-size:18px}
.quote{left:158px;top:1826px;width:884px;text-align:center;font-style:italic;font-size:13px;line-height:24px;color:#4a4643}

/* footer */
.footer{left:0;top:1917px;width:1200px;height:291px;background:var(--footer);color:var(--white)}
.f-col{position:absolute;top:48px}
.f-col h4{font-family:"Montserrat",sans-serif;font-weight:600;font-size:19px;padding-bottom:12px;border-bottom:1px solid var(--footer-line);position:relative}
.f-col h4::after{content:"";position:absolute;left:0;bottom:-1px;width:30px;height:2px;background:var(--green)}
.links{list-style:none;margin-top:17px;font-size:13.5px}
.links li{height:35px;padding-left:16px;position:relative;color:#ddd}
.links li::before{content:"›";position:absolute;left:2px;top:-2px;color:#8d8788}
.links li.on{font-weight:700;color:var(--white)}
.addr{margin-top:17px;font-size:13.5px}
.addr-row{display:flex;gap:12px;margin-bottom:14px;line-height:18px}
.addr-row svg{flex:none;margin-top:2px}
.field{width:228px;background:var(--white);border-radius:2px;color:#555;font-size:10.5px;padding:4px 8px;margin-bottom:8px}
.submit{width:79px;height:26px;background:var(--green);color:var(--white);font-weight:700;font-size:11px;text-align:center;line-height:26px;text-transform:uppercase}
.f-logo{left:880px;top:1970px;width:250px;text-align:center}
.f-logo-dot{width:70px;height:70px;border-radius:50%;background:#5b5657;margin:0 auto 8px}
.f-logo-name{font-family:"Montserrat",sans-serif;font-weight:700;font-size:20px;color:#6d6869;text-transform:uppercase;line-height:1.1}
.social{position:absolute;top:2133px;width:30px;height:30px;border-radius:50%;background:#e9e6e2}
.copyright{left:0;top:2208px;width:1200px;height:56px;background:var(--bottom);color:#ddd;font-size:12.5px;text-align:center;line-height:56px}
</style>
</head>
<body>

<section class="hero abs">
  <div class="hero-photo" role="img" aria-label="Plate of steamed dumplings with green onion on a dark wooden table"></div>
  <header class="topbar"></header>
  <div class="logo-tab">
    <div class="logo-dot"></div>
    <div class="logo-name">Brightfern<br>Foods</div>
  </div>
  <nav class="nav">
    <a class="active">Home</a><a>About Us</a><a>Products</a><a>Contact Us</a>
  </nav>
  <div class="call">
    <div class="call-icon">
      <svg width="22" height="22" viewBox="0 0 24 24"><path fill="#fff" d="M6.6 10.8a15.1 15.1 0 0 0 6.6 6.6l2.2-2.2c.3-.3.7-.4 1-.2 1.1.4 2.3.6 3.6.6.6 0 1 .4 1 1V20c0 .6-.4 1-1 1A17 17 0 0 1 3 4c0-.6.4-1 1-1h3.5c.6 0 1 .4 1 1 0 1.3.2 2.5.6 3.6.1.3 0 .7-.2 1z"/></svg>
    </div>
    <div class="call-text"><b>Call Us:</b><br>(123) 123 456 789</div>
  </div>
  <div class="caption"><h1>The Real Taste of Food</h1></div>
  <svg class="caption-slash abs" width="50" height="92" viewBox="0 0 50 92"><line x1="10" y1="2" x2="46" y2="90" stroke="#7dc21e" stroke-width="5"/></svg>
</section>

<svg class="notch" style="top:598px" width="1200" height="34" viewBox="0 0 1200 34">
  <polygon points="520,32 560,10 600,2 640,10 680,32 680,34 520,34" fill="#eeebe2"/>
  <polyline points="594,16 600,22 606,16" fill="none" stroke="#2a2624" stroke-width="2"/>
</svg>

<h2 class="sec-title" style="top:672px">About Us <em>Brightfern Food</em></h2>
<div class="mark" style="top:721px"></div>
<p class="about-text abs">Lorem ipsum dolor sit amet, consectetuer adipiscing elit, sed diam nonummy nibh euismod tincidunt ut laoreet dolore magna aliquam erat volutpat. Ut wisi enim ad minim veniam, quis nostrud exerci tation ullamcorper suscipit lobortis nisl ut aliquip ex ea commodo consequat. Duis autem vel eum iriure dolor in hendrerit in vulputate velit esse molestie consequat, vel illum dolore eu feugiat nulla facilisis at vero eros et accumsan et iusto odio dignissim qui blandit praesent luptatum zzril delenit augue duis dolore te feugait nulla facilisi.</p>
<a class="btn-more abs"><span>Read Moer</span><i><svg width="12" height="12" viewBox="0 0 12 12"><polyline points="2,2 6,6 2,10" fill="none" stroke="#fff" stroke-width="1.8"/><polyline points="6,2 10,6 6,10" fill="none" stroke="#fff" stroke-width="1.8"/></svg></i></a>

<section class="products abs" role="img" aria-label="Dark wooden board texture">
  <svg class="notch" style="top:0" width="1200" height="32" viewBox="0 0 1200 32">
    <polygon points="520,0 680,0 640,20 600,30 560,20" fill="#eeebe2"/>
  </svg>
  <h2 class="sec-title">Our Products</h2>
  <div class="prod-rule abs"></div>
  <div class="mark" style="top:103px;background:#8f8a84"></div>

  <div class="product" style="left:87px">
    <div class="product-photo" role="img" aria-label="Kimchi dumplings with red onion and lettuce on a black plate"></div>
    <h3>Kimchi<br>Dumplings</h3>
    <div class="plus"><svg width="18" height="18" viewBox="0 0 18 18"><path d="M9 2v14M2 9h14" stroke="#fff" stroke-width="4"/></svg></div>
  </div>
  <div class="product" style="left:429px">
    <div class="product-photo" role="img" aria-label="Plate of kimchi dumplings with green onion"></div>
    <h3>History and Exceptional<br>flavor of Kimchi</h3>
    <div class="plus"><svg width="18" height="18" viewBox="0 0 18 18"><path d="M9 2v14M2 9h14" stroke="#fff" stroke-width="4"/></svg></div>
  </div>
  <div class="product" style="left:772px">
    <div class="product-photo" role="img" aria-label="Steamed buns with red chili on a dark plate"></div>
    <h3>Kimchi<br>Dumplings</h3>
    <div class="plus"><svg width="18" height="18" viewBox="0 0 18 18"><path d="M9 2v14M2 9h14" stroke="#fff" stroke-width="4"/></svg></div>
  </div>

  <div class="slide-arrow" style="left:36px"><svg width="12" height="14" viewBox="0 0 12 14"><polyline points="8,2 3,7 8,12" fill="none" stroke="#fff" stroke-width="2"/></svg></div>
  <div class="slide-arrow" style="left:1118px"><svg width="12" height="14" viewBox="0 0 12 14"><polyline points="4,2 9,7 4,12" fill="none" stroke="#fff" stroke-width="2"/></svg></div>

  <svg class="notch" style="top:552px" width="1200" height="32" viewBox="0 0 1200 32">
    <polygon points="520,32 560,10 600,2 640,10 680,32" fill="#eeebe2"/>
    <polyline points="594,14 600,20 606,14" fill="none" stroke="#2a2624" stroke-width="2"/>
  </svg>
</section>

<h2 class="sec-title" style="top:1580px">Client <em>Testimonials</em></h2>
<div class="abs" style="left:385px;top:1639px;width:430px;height:1px;background:var(--paper-line)"></div>
<div class="mark" style="top:1628px"></div>
<svg class="abs" style="left:114px;top:1708px" width="22" height="30" viewBox="0 0 22 30"><polyline points="16,4 6,15 16,26" fill="none" stroke="#cfcac0" stroke-width="3"/></svg>
<svg class="abs" style="left:1066px;top:1708px" width="22" height="30" viewBox="0 0 22 30"><polyline points="6,4 16,15 6,26" fill="none" stroke="#cfcac0" stroke-width="3"/></svg>
<div class="avatar abs" role="img" aria-label="Client portrait photo"></div>
<div class="client-name abs">Vestibulum porta</div>
<p class="quote abs">Lorem ipsum dolor sit amet, consectetur adipiscing elit. Integer venenatis tincidunt elit, aliquam semper quam pulvinar id. Aliquam erat volutpat. Integer nulla urna, sagittis sed viverra quis, tincidunt vel felis. Pellentesque eleifend sem ut diam bibendum, non sagittis sapien pellentesque. Etiam semper</p>

<footer class="footer abs">
  <div class="f-col" style="left:109px;width:122px">
    <h4>Quick Links</h4>
    <ul class="links">
      <li class="on">Home</li><li>About Us</li><li>Products</li><li>Contact Us</li>
    </ul>
  </div>
  <div class="abs" style="left:287px;top:95px;width:1px;height:150px;background:var(--footer-line)"></div>
  <div class="f-col" style="left:334px;width:214px">
    <h4>Address</h4>
    <div class="addr">
      <div class="addr-row">
        <svg width="12" height="16" viewBox="0 0 12 16"><path fill="#fff" d="M6 0a6 6 0 0 0-6 6c0 4.5 6 10 6 10s6-5.5 6-10a6 6 0 0 0-6-6zm0 8.5A2.5 2.5 0 1 1 6 3.5a2.5 2.5 0 0 1 0 5z"/></svg>
        <div style="font-size:12.5px"><b>Brightfern Food</b><br>Dolor sit amet, consectetuer<br>adipiscing elit, sed diam123456</div>
      </div>
      <div class="addr-row">
        <svg width="13" height="13" viewBox="0 0 24 24"><path fill="#fff" d="M6.6 10.8a15.1 15.1 0 0 0 6.6 6.6l2.2-2.2c.3-.3.7-.4 1-.2 1.1.4 2.3.6 3.6.6.6 0 1 .4 1 1V20c0 .6-.4 1-1 1A17 17 0 0 1 3 4c0-.6.4-1 1-1h3.5c.6 0 1 .4 1 1 0 1.3.2 2.5.6 3.6.1.3 0 .7-.2 1z"/></svg>
        <div>(123) 123 456 7890</div>
      </div>
      <div class="addr-row">
        <svg width="14" height="11" viewBox="0 0 14 11"><rect x="0" y="0" width="14" height="11" fill="#fff"/><polyline points="0,0 7,6 14,0" fill="none" stroke="#272324" stroke-width="1.4"/></svg>
        <div>info@brightfernfood.com</div>
      </div>
    </div>
  </div>
  <div class="abs" style="left:589px;top:95px;width:1px;height:150px;background:var(--footer-line)"></div>
  <div class="f-col" style="left:638px;width:228px">
    <h4>Get in Touch</h4>
    <div style="margin-top:16px">
      <div class="field" style="height:24px">Name</div>
      <div class="field" style="height:24px">Email</div>
      <div class="field" style="height:41px">Message</div>
      <div class="submit">Submit</div>
    </div>
  </div>
</footer>
<div class="f-logo abs">
  <div class="f-logo-dot"></div>
  <div class="f-logo-name">Brightfern<br>Foods</div>
</div>
<div class="social" style="left:931px"></div>
<div class="social" style="left:975px"></div>
<div class="social" style="left:1020px"></div>
<div class="social" style="left:1068px"></div>
<div class="copyright abs">Copyright © 2016 Brightfern Food . All Rights Reserved</div>

</body>
</html>
```